Top business card designs - show off your work!

Calling all [url removed, login to view] designers! We are giving away $1000 to the best business card design on [url removed, login to view]!

Why enter? 2 reasons:
1) $1000 main prize for the best design
2) The chance to show off your best designs to prospective employers - we will not be sealing the contest.

Here's the rules:
1) Designs should not infringe on the copyright of any existing company or designer
2) Designs should not include real personal details (use fake names and details like Alan Brewer)
3) You may include designs you have done for previous clients

Good luck!!!

```html
<!DOCTYPE html>
<html lang="en">
<head>
<meta charset="utf-8">
<title>Corrin Hale Leather – Business Cards</title>
<link rel="stylesheet" href="https://fonts.googleapis.com/css2?family=Open+Sans:wght@300;400;600&display=swap">
<style>
  :root {
    --backdrop: #e6e3df;
    --card-leather: #4d2a23;
    --card-ink: #ffffff;
    --card-ink-soft: rgba(255,255,255,0.85);
    --card-shadow: rgba(40, 20, 15, 0.28);
  }
  * { box-sizing: border-box; margin: 0; padding: 0; }
  html, body {
    width: 1200px;
    height: 873px;
    overflow: hidden;
    background: var(--backdrop);
    font-family: "Open Sans", Arial, sans-serif;
  }
  .sheet {
    width: 1200px;
    height: 873px;
    display: flex;
    align-items: center;
    justify-content: center;
    gap: 44px;
  }
  .card {
    position: relative;
    width: 528px;
    height: 302px;
    background: var(--card-leather);
    color: var(--card-ink);
    border-radius: 4px;
    box-shadow: 0 14px 30px var(--card-shadow);
  }

  /* Contact side */
  .brand-mini {
    position: absolute;
    left: 34px;
    top: 32px;
    display: flex;
    align-items: center;
    gap: 10px;
  }
  .brand-mini__dot {
    width: 22px;
    height: 22px;
    border: 2px solid var(--card-ink);
    border-radius: 50%;
  }
  .brand-mini__name {
    font-size: 13px;
    font-weight: 600;
    letter-spacing: 0.08em;
    text-transform: uppercase;
  }
  .holder {
    position: absolute;
    right: 34px;
    top: 108px;
    left: 34px;
    text-align: right;
  }
  .holder__name {
    font-size: 24px;
    font-weight: 300;
    letter-spacing: 0.01em;
    padding-bottom: 10px;
  }
  .holder__rule {
    height: 2px;
    background: var(--card-ink);
    margin-left: 150px;
  }
  .contact-list {
    position: absolute;
    left: 34px;
    top: 168px;
    list-style: none;
    font-size: 13px;
    font-weight: 400;
    color: var(--card-ink-soft);
  }
  .contact-list__item {
    display: flex;
    align-items: flex-start;
    gap: 12px;
    line-height: 17px;
    margin-bottom: 7px;
  }
  .contact-list__icon {
    width: 14px;
    height: 14px;
    flex: none;
    margin-top: 1px;
    fill: var(--card-ink);
  }

  /* Brand side */
  .card--brand {
    display: flex;
    align-items: center;
    justify-content: center;
  }
  .brand-lockup {
    display: flex;
    align-items: center;
    gap: 18px;
  }
  .brand-lockup__ring {
    width: 54px;
    height: 54px;
    border: 3px solid var(--card-ink);
    border-radius: 50%;
  }
  .brand-lockup__name {
    font-size: 26px;
    font-weight: 600;
    letter-spacing: 0.1em;
    text-transform: uppercase;
    line-height: 1.2;
  }
</style>
</head>
<body>
<main class="sheet">

  <section class="card card--contact" aria-label="Business card, contact side">
    <div class="brand-mini">
      <span class="brand-mini__dot"></span>
      <span class="brand-mini__name">Corrin Hale Leather</span>
    </div>

    <div class="holder">
      <p class="holder__name">Alan Brewer</p>
      <div class="holder__rule"></div>
    </div>

    <ul class="contact-list">
      <li class="contact-list__item">
        <svg class="contact-list__icon" viewBox="0 0 16 16" aria-hidden="true"><path d="M3.6 1.2l2.3 2.6-1.3 1.9c.8 1.9 2.7 3.8 4.7 4.7l1.9-1.3 2.6 2.3-1.3 2.3C8 14.4 1.6 8 1.3 2.5z"/></svg>
        <span>0400 555 018</span>
      </li>
      <li class="contact-list__item">
        <svg class="contact-list__icon" viewBox="0 0 16 16" aria-hidden="true"><path d="M1 3h14v10H1z M2.2 4.2V5L8 9l5.8-4v-.8z" fill-rule="evenodd"/></svg>
        <span>alan@corrinhale.com</span>
      </li>
      <li class="contact-list__item">
        <svg class="contact-list__icon" viewBox="0 0 16 16" aria-hidden="true"><path d="M8 1a7 7 0 100 14A7 7 0 008 1zm0 1.3c.7.7 1.3 2 1.6 3.4H6.4C6.7 4.3 7.3 3 8 2.3zM2.5 7h2.6c0 .7 0 1.4.1 2H2.5a5.7 5.7 0 010-2zm1 3.3h1.9c.2 1 .5 1.8.9 2.5a5.7 5.7 0 01-2.8-2.5zm2.9 0h3.2C9.3 11.7 8.7 13 8 13.7c-.7-.7-1.3-2-1.6-3.4zM6.4 9c-.1-.6-.1-1.3 0-2h3.2c.1.7.1 1.4 0 2zm4.3 0c.1-.6.1-1.3.1-2h2.7a5.7 5.7 0 010 2zm-.5 1.3h1.9a5.7 5.7 0 01-2.8 2.5c.4-.7.7-1.5.9-2.5zm1.9-4.6h-2c-.2-1-.5-1.8-.9-2.5a5.7 5.7 0 012.9 2.5zM6.2 3.2c-.4.7-.7 1.5-.9 2.5H3.5a5.7 5.7 0 012.7-2.5z"/></svg>
        <span>www.corrinhale.com</span>
      </li>
      <li class="contact-list__item">
        <svg class="contact-list__icon" viewBox="0 0 16 16" aria-hidden="true"><path d="M8 1.5l7 6h-2v7H9.8v-4.5H6.2v4.5H3v-7H1z"/></svg>
        <span>PO Box 48, Seabrook<br>Tasmania, Australia 7000</span>
      </li>
    </ul>
  </section>

  <section class="card card--brand" aria-label="Business card, brand side">
    <div class="brand-lockup">
      <span class="brand-lockup__ring"></span>
      <span class="brand-lockup__name">Corrin Hale<br>Leather</span>
    </div>
  </section>

</main>
</body>
</html>
```